Vision / Mission Poster Required

We are looking to display our company Vision / Mission / Values on a poster. This will be displayed in the head office and other site offices.

The document needs to look professional however still be fun, eye catching and easy to read. It will be predominantly displayed in A3 format.

The design needs to use our company Logo which is attached along with the Text to display on the poster. I have put some additional text on the doc that you can include if it suits the layout but is not essential.

Target Market(s)

Staff, Corporate Visitors

Industry/Entity Type

Electric Company

Font styles to use
Sans Serif

Colors

Designer to choose colors to be used in the design.

Requirements
Must have
• Incorporate Logo
• Professional Look
• Attention grabbing
• Easy to Read
Should not have
• Lightning Bolts
• Pictures of random people/Things

```html
<!DOCTYPE html>
<html lang="en">
<head>
<meta charset="utf-8">
<title>Lumen Grid Electrical – Vision, Mission and Values</title>
<link rel="stylesheet" href="https://fonts.googleapis.com/css2?family=Open+Sans:wght@400;600;700;800&display=swap">
<style>
  :root {
    --navy: #1f3f73;
    --orange: #ec6a1f;
    --ink: #1d1d1d;
    --paper: #ffffff;
    --header-light: #eef0f3;
  }
  * { box-sizing: border-box; margin: 0; padding: 0; }
  html, body { width: 923px; height: 1200px; overflow: hidden; background: var(--paper); }
  body { font-family: "Open Sans", Arial, sans-serif; color: var(--ink); position: relative; }

  .header { position: absolute; left: 0; top: 0; width: 923px; height: 96px; }
  .header-bg { position: absolute; left: 0; top: 0; }
  .brand { position: absolute; left: 30px; top: 18px; display: flex; align-items: center; gap: 12px; }
  .brand-dot { width: 46px; height: 46px; border-radius: 50%; background: var(--orange); flex: none; }
  .brand-name { font-weight: 800; font-size: 24px; color: var(--navy); line-height: 1.05; letter-spacing: .5px; }
  .site { position: absolute; right: 28px; top: 28px; color: #fff; font-size: 20px; line-height: 24px; display: flex; align-items: center; gap: 9px; }
  .site-icon { flex: none; }

  .hero { position: absolute; left: 0; top: 96px; width: 923px; height: 422px;
    background: linear-gradient(90deg, #2a241c 0%, #4a3f30 32%, #a2856a 50%, #d9a24a 62%, #c85f8a 76%, #4fa0b4 88%, #e7b63c 100%); }
  .hero::after { content: ""; position: absolute; inset: 0; background: linear-gradient(90deg, rgba(0,0,0,.35), rgba(0,0,0,.05) 70%); }
  .vision { position: absolute; left: 30px; top: 150px; color: #fff; font-weight: 700; line-height: 1; text-shadow: 0 2px 6px rgba(0,0,0,.4); z-index: 1; }
  .vision .v1 { font-size: 60px; margin-left: 4px; }
  .vision .v2 { font-size: 31px; margin: 6px 0 0 8px; }
  .vision .v3 { font-size: 50px; margin-top: 2px; }
  .vision .v4 { font-size: 62px; margin-top: 2px; }

  .pill { position: absolute; left: 50%; transform: translateX(-50%); width: 200px; height: 42px;
    background: var(--navy); color: var(--orange); font-weight: 600; font-size: 29px;
    display: flex; align-items: center; justify-content: center; border-radius: 4px;
    box-shadow: 0 3px 5px rgba(0,0,0,.3); }
  .pill-mission { top: 540px; }
  .pill-values { top: 790px; }

  .mission-list { position: absolute; left: 32px; right: 28px; top: 598px; list-style: none; }
  .mission-list li { position: relative; padding-left: 44px; margin-bottom: 8px; font-size: 15.5px; line-height: 1.3; }
  .mission-list .num { position: absolute; left: 2px; top: 1px; width: 20px; height: 20px; border-radius: 50%;
    background: var(--navy); border: 2px solid var(--orange); color: #fff; font-size: 11px; font-weight: 700;
    display: flex; align-items: center; justify-content: center; }
  .item-title { font-weight: 700; display: block; }

  .values-list { position: absolute; left: 30px; right: 40px; top: 852px; list-style: none; }
  .values-list li { position: relative; padding-left: 40px; margin-bottom: 4px; font-size: 15.5px; line-height: 1.3; }
  .values-list li::before { content: ""; position: absolute; left: 0; top: 7px; width: 8px; height: 8px; border-radius: 50%; background: var(--orange); }

  .footer-band { position: absolute; left: 0; bottom: 0; width: 923px; height: 11px; display: flex; }
  .footer-band .navy { width: 695px; background: var(--navy); }
  .footer-band .orange { flex: 1; background: var(--orange); }
</style>
</head>
<body>
  <header class="header">
    <svg class="header-bg" width="923" height="96" viewBox="0 0 923 96" aria-hidden="true">
      <rect width="923" height="96" fill="var(--header-light)"/>
      <polygon points="398,0 923,0 923,84 352,84" fill="var(--navy)"/>
      <polygon points="352,84 923,84 923,96 0,96 0,90 346,90" fill="var(--orange)"/>
    </svg>
    <div class="brand">
      <span class="brand-dot"></span>
      <span class="brand-name">LUMEN GRID<br>ELECTRICAL</span>
    </div>
    <div class="site">
      <svg class="site-icon" width="18" height="18" viewBox="0 0 18 18" aria-hidden="true" fill="none" stroke="#fff" stroke-width="1.5">
        <circle cx="9" cy="9" r="7.5"/><ellipse cx="9" cy="9" rx="3.2" ry="7.5"/><line x1="1.5" y1="9" x2="16.5" y2="9"/>
      </svg>
      <span>www.lumengrid-example.com.au</span>
    </div>
  </header>

  <section class="hero" role="img" aria-label="Photo of a shopping arcade walkway with a colourful mural wall and yellow ceiling panels">
  </section>
  <h1 class="vision">
    <div class="v1">VISION</div>
    <div class="v2">TO BE PERTH'S PREMIER</div>
    <div class="v3">PROVIDER OF ELECTRICAL</div>
    <div class="v4">SERVICE SOLUTIONS</div>
  </h1>

  <h2 class="pill pill-mission">Mission</h2>
  <ol class="mission-list">
    <li><span class="num">1</span><span class="item-title">Deliver Growth and Value</span>By: - Maintaining a market presence - Leveraging our technical resources – Networking and developing stakeholder relationships</li>
    <li><span class="num">2</span><span class="item-title">Remain Profitable</span>By: - Increasing revenue – Optimizing capacity utilization – Maintaining expenses</li>
    <li><span class="num">3</span><span class="item-title">Be Sustainable</span>By: - Improving internal efficiency – Diversifying our income sources – Implementing Social &amp; Environmental improvement initiatives</li>
  </ol>

  <h2 class="pill pill-values">Values</h2>
  <ul class="values-list">
    <li><span class="item-title">Honesty &amp; Integrity</span>Customers, contractors and suppliers will be able to count on Lumen Grid personnel to deal straightforwardly and adhere to the strictest moral and ethical codes of conduct.</li>
    <li><span class="item-title">Safety &amp; Responsibility</span>Lumen Grid is committed to constantly improving safety practices at project job sites and within the electrical service industry as a whole.</li>
    <li><span class="item-title">Commitment to Quality</span>Customers and stakeholders will be able to count on Lumen Grid's workmanship being among the best in the industry.</li>
    <li><span class="item-title">Innovation &amp; Technology</span>Customers can rely on us to apply the latest proven technologies on their projects, and to be on the ground floor of industry standards for new and emerging markets.</li>
    <li><span class="item-title">Knowledgeable &amp; Valued Employees</span>Lumen Grid recognizes that its greatest asset is its people. We pledge to treat each employee with integrity, dealing honestly with all.</li>
  </ul>

  <div class="footer-band"><span class="navy"></span><span class="orange"></span></div>
</body>
</html>
```